Harborlight Capital Estates business card

We are a real estate advisory and investment company. We are specialized in assisting high networth individuals to invest in real estate overseas. We deliver a very personalized service, anticipating all the potential challenges an investor can face, and making it easy and safe for them. We also co-invest with our clients, assuring them that each project will be looked after as it is our own, and at the same time giving them the extra booth on confidence to invest.

We need a business card design. The business card must have a very premium, high-end look, reflecting principles like "commitment", "trust" and "timeless (but contemporary)". We look for long term relationships with our clients, and we grow with their referrals. We are all about conquering the confidence of the clients by always delivering above the expectations performance.

Target Market(s)

High net worth individuals.

Industry/Entity Type

Real Estate

Contact Information for Business Card

Please consider places on the business card for:

Name
Function (bellow name in smaller size text)

Mobile phone
E-mail
Skype ID
WeChat ID

Adress (3 lines)

Also include the following locations references:
PORTUGAL * DUBAI * HONG KONG

Website: www.hcestates-example.com

Requirements
Must have
• Company Logo

```html
<!DOCTYPE html>
<html lang="en">
<head>
<meta charset="utf-8">
<title>Harborlight Capital Estates – Business Card</title>
<link rel="stylesheet" href="https://fonts.googleapis.com/css2?family=Open+Sans:wght@400;600&display=swap">
<style>
  :root {
    --brand-blue: #29a9e0;
    --ink: #444444;
    --paper: #ffffff;
    --backdrop: #e8e5e1;
    --rule: #b9b9b9;
  }
  * { box-sizing: border-box; margin: 0; padding: 0; }
  html, body { width: 1200px; height: 1000px; overflow: hidden; }
  body {
    background: var(--backdrop);
    font-family: "Open Sans", Arial, sans-serif;
    position: relative;
  }
  .card {
    position: absolute;
    left: 265px;
    width: 665px;
    height: 397px;
    box-shadow: 0 3px 10px rgba(0,0,0,0.18);
  }
  .card--front { top: 73px; background: var(--paper); }
  .card--back { top: 533px; background: var(--brand-blue); }

  .wordmark {
    position: absolute;
    text-align: center;
    font-weight: 600;
    line-height: 1.15;
  }
  .card--front .wordmark {
    left: 30px; width: 300px; top: 150px;
    color: var(--brand-blue);
    font-size: 27px;
  }
  .card--back .wordmark {
    left: 0; width: 100%; top: 155px;
    color: var(--paper);
    font-size: 38px;
  }

  .divider {
    position: absolute;
    left: 360px; top: 82px;
    width: 1px; height: 235px;
    background: var(--rule);
  }

  .contact {
    position: absolute;
    left: 395px; top: 70px;
    color: var(--ink);
    font-size: 16px;
    line-height: 21px;
  }
  .contact__name { color: var(--brand-blue); font-size: 20px; line-height: 24px; }
  .contact__role { margin-bottom: 19px; }
  .contact__address { margin-bottom: 19px; }
  .contact__list { list-style: none; line-height: 22px; }
  .contact__list li { display: flex; align-items: center; gap: 5px; }
  .contact__list svg { width: 16px; height: 16px; flex: none; }

  .locations {
    position: absolute;
    left: 0; bottom: 0;
    width: 100%; height: 32px;
    background: var(--brand-blue);
    color: var(--paper);
    font-size: 15px;
    letter-spacing: 5px;
    line-height: 32px;
    text-align: center;
    word-spacing: 12px;
  }
</style>
</head>
<body>
  <section class="card card--front">
    <div class="wordmark">Harborlight<br>Capital Estates</div>
    <div class="divider"></div>
    <div class="contact">
      <div class="contact__name">Daniel Whitmore</div>
      <div class="contact__role">Manager</div>
      <div class="contact__address">412 Linden Park Ave<br>Suite 210<br>Easton, Vermont 05901</div>
      <ul class="contact__list">
        <li><svg viewBox="0 0 16 16"><circle cx="8" cy="8" r="7" fill="var(--brand-blue)"/></svg>hcestates</li>
        <li><svg viewBox="0 0 16 16"><circle cx="8" cy="8" r="7" fill="var(--brand-blue)"/></svg>hcestates</li>
        <li><svg viewBox="0 0 16 16"><path d="M3 5c0-1.5 1-2.5 2.5-2.5h5C12 2.5 13 3.5 13 5v1h-3V4.5H6V6H3z M4 8l2.5-2h3L12 8v5H4z" fill="var(--brand-blue)"/><circle cx="8" cy="10" r="1.5" fill="#fff"/></svg>000 000 000</li>
        <li><svg viewBox="0 0 16 16"><rect x="1.5" y="3.5" width="13" height="9" fill="var(--brand-blue)"/><path d="M1.5 3.5 8 9l6.5-5.5" fill="none" stroke="#fff" stroke-width="1.2"/></svg>info@hcestates-example.com</li>
        <li><svg viewBox="0 0 16 16"><circle cx="8" cy="8" r="6.5" fill="none" stroke="var(--brand-blue)" stroke-width="1.6"/><path d="M1.5 8h13M8 1.5c-3 3.5-3 9.5 0 13M8 1.5c3 3.5 3 9.5 0 13" fill="none" stroke="var(--brand-blue)" stroke-width="1.2"/></svg>www.hcestates-example.com</li>
      </ul>
    </div>
    <div class="locations">PORTUGAL - DUBAI - HONG KONG</div>
  </section>

  <section class="card card--back">
    <div class="wordmark">Harborlight<br>Capital Estates</div>
  </section>
</body>
</html>
```